Website design for a private chef business

Need a website that is eye catching and with easy contact, newsletter signups and scheduling tool/calendar . Website is platerbv.com and geographic focus is The Woodlands, TX and Austin, TX. I cook all styles of cuisine so anything is possible and I'm a veteran of Afghanistan via the Tarn Guard so if you could mention it's a veteran owned business

Target Market(s)

Affluent families and successful professionals in TheWoodlands, TX and Austin, TX

Industry/Entity Type

Business

Number of Pages Required

1 page

Requirements
Must have
• Eyecatching visuals
• Contact form
• Newsletter sign up
• Scheduling tool
Should not have
• N/a

```html
<!DOCTYPE html>
<html lang="en">
<head>
<meta charset="utf-8">
<title>Platerbv – Private Chef</title>
<link href="https://fonts.googleapis.com/css2?family=Courgette&family=Open+Sans:wght@400;600&family=Roboto+Condensed:wght@700&display=swap" rel="stylesheet">
<style>
:root{
  --green:#67b936;
  --green-btn:#4cb846;
  --green-text:#5aae2c;
  --dark:#1c1c1c;
  --nav-active:#3e3e3e;
  --ink:#444;
  --muted:#777;
  --panel:#f3f2ec;
  --line:#dcdcdc;
  --footer-bar:#2b2b2b;
  --white:#fff;
}
*{margin:0;padding:0;box-sizing:border-box}
html,body{width:685px;height:1200px;overflow:hidden;background:var(--white)}
body{position:relative;font-family:"Open Sans",sans-serif;color:var(--ink)}
.abs{position:absolute}
.script{font-family:"Courgette",cursive}

/* header */
.site-header{left:0;top:0;width:685px;height:64px;background:var(--green)}
.brand{left:56px;top:22px;color:var(--white);font-family:"Courgette",cursive;font-size:17px}
.header-phone{left:470px;top:15px;color:var(--white);font-family:"Courgette",cursive;font-size:11px;display:flex;align-items:center;gap:5px}
.quick-contact{left:559px;top:11px;width:70px;height:21px;border:1px solid var(--white);border-radius:2px;color:var(--white);font-family:"Courgette",cursive;font-size:9.5px;display:flex;align-items:center;justify-content:center}
.main-nav{left:337px;top:36px;height:28px;display:flex;font-size:7.5px;color:var(--white)}
.main-nav a{color:inherit;text-decoration:none;padding:0 10px;display:flex;align-items:center}
.main-nav a.active{background:var(--nav-active);padding:0 12px;margin-right:6px}

/* hero */
.hero-photo{left:0;top:64px;width:685px;height:317px;background:linear-gradient(90deg,#d9d6d0 0%,#ece9e4 40%,#f5f3f0 55%,#cfccc6 80%,#b9b4ac 100%)}
.hero-title{left:73px;top:145px;font-family:"Courgette",cursive;color:var(--green-text);font-size:40px;line-height:1}
.hero-sub{left:76px;top:190px;font-family:"Courgette",cursive;color:#3a3a3a;font-size:23px;line-height:1}
.signup-btn{left:74px;top:234px;width:78px;height:21px;background:var(--green-btn);border:1px solid #8fd26a;color:var(--white);font-size:7.5px;font-weight:600;display:flex;align-items:center;justify-content:center}
.slide-arrow{top:198px;width:20px;height:20px;border-radius:50%;background:rgba(120,120,120,.55)}

/* quote */
.quote-panel{left:56px;top:328px;width:572px;height:89px;background:var(--panel);border-top:2px solid var(--green)}
.quote-card{left:56px;top:417px;width:572px;height:70px;background:var(--white)}
.quote-title{left:0;top:342px;width:685px;text-align:center;font-family:"Roboto Condensed",sans-serif;font-size:19px;color:var(--green-text)}
.field{top:373px;width:99px;height:23px;background:var(--white);border:1px solid var(--line);font-size:7px;color:#666;padding-left:10px;display:flex;align-items:center}
.quote-btn{left:521px;top:373px;width:71px;height:23px;background:var(--green-btn);color:var(--white);font-size:7.5px;display:flex;align-items:center;justify-content:center}

/* welcome */
.welcome-rule{top:455px;height:1px;background:#e2e2e2;width:64px}
.welcome-title{left:0;top:434px;width:685px;text-align:center;font-size:25px;color:#3a3a3a}
.welcome-title span{color:var(--green-text)}
.welcome-sub{left:0;top:466px;width:685px;text-align:center;font-size:9px;color:#555}
.welcome-copy{left:88px;top:487px;width:509px;text-align:center;font-size:6.4px;line-height:12px;color:var(--muted)}

/* chefs */
.chefs-section{left:0;top:548px;width:685px;height:290px;background:radial-gradient(ellipse at 50% 40%,#2d2d2d,#121212)}
.chefs-title{left:0;top:566px;width:685px;text-align:center;color:var(--white);font-size:23px}
.chefs-intro{left:200px;top:600px;width:285px;text-align:center;color:var(--white);font-size:7px;line-height:12px}
.chef{top:642px;width:190px;text-align:center;color:var(--white)}
.chef-photo{width:94px;height:94px;margin:0 auto;border-radius:50%;border:2px solid #ddd;background:linear-gradient(180deg,#c9c3b8,#e8e6e2 55%,#f4f4f4)}
.chef-name{margin-top:11px;font-family:"Courgette",cursive;font-size:10.5px}
.chef-bio{margin-top:5px;font-size:6.4px;line-height:12px}
.chef-more{margin-top:4px}

/* news */
.news-heading{left:56px;top:861px;font-size:11.5px;color:#333;letter-spacing:.2px}
.news-thumb{top:893px;width:107px;height:94px;border:3px solid #eee;background:linear-gradient(135deg,#8d8377,#d8d4cd 55%,#efe9df)}
.news-body{top:890px;width:140px}
.news-title{font-size:8.8px;color:#333}
.news-date{margin-top:8px;font-size:8px;color:var(--green-text)}
.news-excerpt{margin-top:5px;font-size:6.2px;line-height:12px;color:#555}
.news-more{margin-top:6px;font-size:6.5px;color:#333}

/* footer */
.site-footer{left:0;top:1021px;width:685px;height:145px;background:linear-gradient(180deg,#6cbb3c,#5fae33)}
.contact-item{top:1039px;display:flex;align-items:center;gap:9px;color:var(--white);font-size:6.8px;line-height:11px}
.contact-icon{width:19px;height:19px;border:1px solid rgba(255,255,255,.8);border-radius:50%;display:flex;align-items:center;justify-content:center;flex:none}
.contact-item strong{font-weight:600;font-size:7.5px}
.footer-rule{left:122px;top:1072px;width:508px;height:1px;background:rgba(255,255,255,.35)}
.footer-divider{left:350px;top:1078px;width:1px;height:76px;background:rgba(255,255,255,.35)}
.footer-label{top:1091px;color:var(--white);font-family:"Courgette",cursive;font-size:12px}
.newsletter-input{left:126px;top:1117px;width:188px;height:25px;border:1px solid rgba(255,255,255,.85);color:var(--white);font-size:6.2px;padding-left:8px;display:flex;align-items:center;justify-content:space-between;padding-right:8px}
.footer-brand{left:376px;top:1115px;color:var(--white);font-family:"Courgette",cursive;font-size:13px}
.social{top:1118px;width:21px;height:21px;border:1px solid rgba(255,255,255,.9);border-radius:50%}
.bottom-bar{left:0;top:1166px;width:685px;height:34px;background:var(--footer-bar);color:#ddd;font-size:6.3px;display:flex;align-items:center;justify-content:center}
</style>
</head>
<body>

<header class="abs site-header"></header>
<div class="abs brand">Platerbv</div>
<div class="abs header-phone">
  <svg width="9" height="9" viewBox="0 0 24 24"><path fill="#fff" d="M6.6 10.8a15.1 15.1 0 0 0 6.6 6.6l2.2-2.2c.3-.3.7-.4 1-.2 1.1.4 2.3.6 3.6.6.6 0 1 .4 1 1V20c0 .6-.4 1-1 1A17 17 0 0 1 3 4c0-.6.4-1 1-1h3.5c.6 0 1 .4 1 1 0 1.3.2 2.5.6 3.6.1.3 0 .7-.2 1z"/></svg>
  1.512.555.0148
</div>
<div class="abs quick-contact">Quick Contact</div>
<nav class="abs main-nav">
  <a class="active" href="#">HOME</a>
  <a href="#">ABOUT US</a>
  <a href="#">OUR CHEFS</a>
  <a href="#">NEWS</a>
  <a href="#">CONTACT US</a>
</nav>

<div class="abs hero-photo" role="img" aria-label="Smiling chef in white hat and jacket holding wooden kitchen utensils in a bright blurred kitchen"></div>
<div class="abs hero-title">A veteran</div>
<div class="abs hero-sub">owned business</div>
<div class="abs signup-btn">SIGN UP FREE</div>
<div class="abs slide-arrow" style="left:17px">
  <svg width="20" height="20" viewBox="0 0 20 20"><path d="M11.5 6 7.5 10l4 4" stroke="#fff" stroke-width="1.4" fill="none"/></svg>
</div>
<div class="abs slide-arrow" style="left:647px">
  <svg width="20" height="20" viewBox="0 0 20 20"><path d="M8.5 6l4 4-4 4" stroke="#fff" stroke-width="1.4" fill="none"/></svg>
</div>

<section>
  <div class="abs quote-panel"></div>
  <div class="abs quote-card"></div>
  <h2 class="abs quote-title">GET A QUOTE</h2>
  <div class="abs field" style="left:92px">Name</div>
  <div class="abs field" style="left:199px">E - Mail</div>
  <div class="abs field" style="left:307px">Phone</div>
  <div class="abs field" style="left:415px;justify-content:space-between;padding-right:8px">Choose a families
    <svg width="6" height="4" viewBox="0 0 6 4"><path d="M.5.5 3 3 5.5.5" stroke="#888" fill="none"/></svg>
  </div>
  <div class="abs quote-btn">GET A QUOTE</div>
</section>

<section>
  <div class="abs welcome-rule" style="left:178px"></div>
  <div class="abs welcome-rule" style="left:443px"></div>
  <h2 class="abs welcome-title script">Welcome to <span>platerbv</span></h2>
  <p class="abs welcome-sub">We focus on rich families in Woodlands &amp; Austin city in Texas</p>
  <p class="abs welcome-copy">Lorem ipsum dolor sit amet, consectetur adipiscing elit, sed do eiusmod tempor incididunt ut labore et dolore magna aliqua. Ut enim ad minim veniam, quis nostrud exercitation ullamco laboris nisi ut aliquip ex ea commodo consequat. Duis aute irure dolor in reprehenderit in voluptate velit esse cillum dolore eu fugiat nulla pariatur. Excepteur sint occaecat cupidatat non proident, sunt in culpa qui officia deserunt mollit anim id est laborum</p>
</section>

<section>
  <div class="abs chefs-section" role="img" aria-label="Dark kitchen backdrop with a chef and fresh vegetables"></div>
  <h2 class="abs chefs-title script">Our Chefs</h2>
  <p class="abs chefs-intro">Lorem ipsum dolor sit amet, consectetur adipiscing elit, sed do eiusmod tempor incididunt ut labore et dolore magna aliqua.</p>

  <div class="abs chef" style="left:47px">
    <div class="chef-photo" role="img" aria-label="Portrait of a chef in white hat"></div>
    <div class="chef-name">Marisol Keane</div>
    <p class="chef-bio">Lorem ipsum dolor sit amet, conse adipisic ing elit,<br>sed do eiusmod tempor incididunt</p>
    <svg class="chef-more" width="8" height="8" viewBox="0 0 8 8"><path d="M1 1l3 2.5L7 1M1 4.5 4 7l3-2.5" stroke="#fff" fill="none"/></svg>
  </div>
  <div class="abs chef" style="left:236px">
    <div class="chef-photo" role="img" aria-label="Portrait of a chef in white hat"></div>
    <div class="chef-name">Marisol Keane</div>
    <p class="chef-bio">Lorem ipsum dolor sit amet, conse adipisic ing elit,<br>sed do eiusmod tempor incididunt</p>
    <svg class="chef-more" width="8" height="8" viewBox="0 0 8 8"><path d="M1 1l3 2.5L7 1M1 4.5 4 7l3-2.5" stroke="#fff" fill="none"/></svg>
  </div>
  <div class="abs chef" style="left:428px">
    <div class="chef-photo" role="img" aria-label="Portrait of a chef in white hat"></div>
    <div class="chef-name">Marisol Keane</div>
    <p class="chef-bio">Lorem ipsum dolor sit amet, conse adipisic ing elit,<br>sed do eiusmod tempor incididunt</p>
    <svg class="chef-more" width="8" height="8" viewBox="0 0 8 8"><path d="M1 1l3 2.5L7 1M1 4.5 4 7l3-2.5" stroke="#fff" fill="none"/></svg>
  </div>
</section>

<section>
  <h2 class="abs news-heading" style="font-weight:400">LATEST NEWS</h2>

  <div class="abs news-thumb" style="left:56px" role="img" aria-label="Chef plating a dish"></div>
  <article class="abs news-body" style="left:177px">
    <h3 class="news-title" style="font-weight:400">Nulla at diam ornare, aliquam urna</h3>
    <div class="news-date">JULY 25, 2015</div>
    <p class="news-excerpt">Nulla at diam ornare, aliquam urna vel, commodo urna. Nam id risus a est luctus consectetur quis eget libero. Suspendisse potenti. Pellentesque habitant morbi tristique senectus</p>
    <div class="news-more">READ MORE +</div>
  </article>

  <div class="abs news-thumb" style="left:359px" role="img" aria-label="Chef preparing food in a kitchen"></div>
  <article class="abs news-body" style="left:480px">
    <h3 class="news-title" style="font-weight:400">Nulla at diam ornare, aliquam urna</h3>
    <div class="news-date">JULY 25, 2015</div>
    <p class="news-excerpt">Nulla at diam ornare, aliquam urna vel, commodo urna. Nam id risus a est luctus consectetur quis eget libero. Suspendisse potenti. Pellentesque habitant morbi tristique senectus</p>
    <div class="news-more">READ MORE +</div>
  </article>
</section>

<footer>
  <div class="abs site-footer"></div>
  <div class="abs contact-item" style="left:131px">
    <span class="contact-icon"><svg width="9" height="9" viewBox="0 0 24 24"><path fill="#fff" d="M12 2a7 7 0 0 0-7 7c0 5 7 13 7 13s7-8 7-13a7 7 0 0 0-7-7zm0 9.5A2.5 2.5 0 1 1 12 6.5a2.5 2.5 0 0 1 0 5z"/></svg></span>
    <span>210 Larkspur Row (Cnr. Elm &amp;<br>Grove St.) The Woodlands, TX</span>
  </div>
  <div class="abs contact-item" style="left:308px">
    <span class="contact-icon"><svg width="9" height="9" viewBox="0 0 24 24"><path fill="#fff" d="M6.6 10.8a15.1 15.1 0 0 0 6.6 6.6l2.2-2.2c.3-.3.7-.4 1-.2 1.1.4 2.3.6 3.6.6.6 0 1 .4 1 1V20c0 .6-.4 1-1 1A17 17 0 0 1 3 4c0-.6.4-1 1-1h3.5c.6 0 1 .4 1 1 0 1.3.2 2.5.6 3.6.1.3 0 .7-.2 1z"/></svg></span>
    <span>Phone :<br><strong>+1 512 555 0190</strong></span>
  </div>
  <div class="abs contact-item" style="left:445px">
    <span class="contact-icon"><svg width="9" height="9" viewBox="0 0 24 24"><path fill="none" stroke="#fff" stroke-width="2" d="M3 6h18v12H3zM3 6l9 7 9-7"/></svg></span>
    <span>E-mail:<br><strong style="font-weight:400;font-size:8px">info@platerbv.com</strong></span>
  </div>
  <div class="abs footer-rule"></div>
  <div class="abs footer-divider"></div>

  <div class="abs footer-label" style="left:126px">Newsletter Signup</div>
  <div class="abs newsletter-input">Enter your email address
    <svg width="10" height="10" viewBox="0 0 24 24"><path d="M22 2 2 10l8 3 3 8zM10 13l12-11" stroke="#fff" stroke-width="2" fill="none"/></svg>
  </div>

  <div class="abs footer-brand">Platerbv</div>
  <div class="abs footer-label" style="left:427px">Get Social with Us</div>
  <div class="abs social" style="left:428px" aria-label="Social link"></div>
  <div class="abs social" style="left:454px" aria-label="Social link"></div>
  <div class="abs social" style="left:479px" aria-label="Social link"></div>
  <div class="abs social" style="left:505px" aria-label="Social link"></div>
  <div class="abs social" style="left:529px" aria-label="Social link"></div>

  <div class="abs bottom-bar">©2014 - 2015 platerbv.com., All Rights Reserved.</div>
</footer>

</body>
</html>
```